Brightwave Audiology Letterhead redesign project

We need a full redesign of our current letterhead to make it consistent with the look and feel of our website design www.brightwaveaudio.com.au. It will need to include all information on the current version attached. The letterhead is used for sending medical reports and general correspondence. It should make use of our corporate colours (purple and teal) as per the logo on the existing file. The letterhead should be bold and eye-catching.

Target Market(s)

Medical practitioners.

Font styles to use
Sans Serif

Requirements
Must have
• It will need to include all information on the current version. Must have a premium, professional, high-end look and feel.
Nice to have
• Bold and eye-catching letterhead that reinforces the Brightwave Audiology brand. To stand out from other traditional letterheads.
Should not have
• The design should not be too cluttered or 'busy'

```html
<!DOCTYPE html>
<html lang="en">
<head>
<meta charset="utf-8">
<title>Brightwave Audiology Letterhead</title>
<link rel="stylesheet" href="https://fonts.googleapis.com/css2?family=Nunito:wght@900&family=Source+Sans+3:wght@400;700&display=swap">
<style>
  :root {
    --brand-purple: #6b3590;
    --brand-teal: #23b08e;
    --ink: #1e1e1e;
    --paper: #ffffff;
    --backdrop: #ecebe8;
  }
  * { margin: 0; padding: 0; box-sizing: border-box; }
  html, body {
    width: 1198px;
    height: 1200px;
    overflow: hidden;
    background: var(--backdrop);
  }
  .letterhead {
    position: absolute;
    left: 161px;
    top: 31px;
    width: 868px;
    height: 1124px;
    background: var(--paper);
    box-shadow: 0 2px 10px rgba(0,0,0,0.12);
  }
  .brand-name {
    position: absolute;
    left: 27px;
    top: 62px;
    font-family: "Source Sans 3", sans-serif;
    font-weight: 700;
    font-size: 30px;
    line-height: 36px;
    color: var(--brand-purple);
    white-space: nowrap;
  }
  .contact-block {
    position: absolute;
    right: 19px;
    top: 64px;
    text-align: right;
    font-family: "Source Sans 3", sans-serif;
    font-style: normal;
    font-size: 12.5px;
    line-height: 15.5px;
    color: var(--ink);
  }
  .contact-block .label { color: var(--brand-purple); }
  .header-rule {
    position: absolute;
    left: 18px;
    top: 124px;
    width: 832px;
    height: 8px;
  }
  .tagline {
    position: absolute;
    left: 0;
    width: 100%;
    top: 1062px;
    text-align: center;
    font-family: "Nunito", sans-serif;
    font-weight: 900;
    font-size: 22.5px;
    letter-spacing: -0.4px;
    color: var(--brand-purple);
    white-space: nowrap;
  }
  .tagline .accent { color: var(--brand-teal); }
</style>
</head>
<body>
  <main class="letterhead">
    <div class="brand-name">Brightwave Audiology</div>

    <address class="contact-block">
      <div><span class="label">CLINIC</span> 48 Larkin Avenue, Ridgeview, Qld 4371</div>
      <div><span class="label">TEL</span> 07 4592 2860 <span class="label">FAX</span> 074592 2861</div>
      <div><span class="label">EMAIL</span> hello@brightwaveaudio.com.au</div>
      <div>www.brightwaveaudio.com.au</div>
    </address>

    <svg class="header-rule" viewBox="0 0 832 8" aria-hidden="true">
      <line x1="0" y1="4" x2="382" y2="4" stroke="var(--brand-purple)" stroke-width="3.5"/>
      <line x1="451" y1="4" x2="832" y2="4" stroke="var(--brand-purple)" stroke-width="3.5"/>
    </svg>

    <p class="tagline">your local <span class="accent">independent</span> hearing solutions specialist</p>
  </main>
</body>
</html>
```